Gentle Harbor Label

We need labels for a new brewery called "Gentle Harbor":

We need one label, that we can slightly change to suit the style of liquid. So far the beers are:
- XPA
- Pale ALe
- IPA
- Black Ale

We want creative, fun labels, nothing traditional. but appropriate to suit all international markets.

Design was promoted in LOGO & not in Design, so we got a lot of logo's but very little designs for bottles/cans.

Gentle Harbor Brewing

```html
<!DOCTYPE html>
<html lang="en">
<head>
<meta charset="utf-8">
<title>Gentle Harbor Label – Pale Ale</title>
<link rel="stylesheet" href="https://fonts.googleapis.com/css2?family=Montserrat:wght@500;700;800&display=swap">
<style>
  :root{
    --navy:#1f2b52;
    --red:#8e0a0c;
    --white:#ffffff;
    --chevron:#e8eaec;
    --gold-light:#f3dc97;
    --gold:#cfb06a;
    --gold-dark:#a88a45;
    --ink:#1d1d1d;
  }
  html,body{margin:0;padding:0;overflow:hidden;background:var(--white);}
  .canvas{position:relative;width:1200px;height:1000px;overflow:hidden;background:var(--white);font-family:"Montserrat",sans-serif;}
  .neck-label{position:absolute;left:200px;top:154px;width:216px;height:140px;}
  .body-label{position:absolute;left:128px;top:392px;width:364px;height:456px;}
  .brand-name{font-family:"Montserrat",sans-serif;font-weight:800;fill:var(--navy);}
  .style-name{font-family:"Montserrat",sans-serif;font-weight:500;fill:var(--white);}
  .brewery-line{font-family:"Montserrat",sans-serif;font-weight:700;}
</style>
</head>
<body>
<main class="canvas">

  <!-- Neck label -->
  <svg class="neck-label" viewBox="0 0 216 140" aria-label="Gentle Harbor neck label, Pale Ale">
    <defs>
      <linearGradient id="neckGold" x1="0" y1="0" x2="1" y2="1">
        <stop offset="0" stop-color="var(--gold-dark)"/>
        <stop offset=".45" stop-color="var(--gold-light)"/>
        <stop offset="1" stop-color="var(--gold)"/>
      </linearGradient>
      <clipPath id="neckInner"><ellipse cx="108" cy="70" rx="93" ry="56"/></clipPath>
    </defs>
    <ellipse cx="108" cy="70" rx="106" ry="68" fill="url(#neckGold)"/>
    <ellipse cx="108" cy="70" rx="98" ry="61" fill="var(--white)"/>
    <g clip-path="url(#neckInner)">
      <rect x="0" y="0" width="216" height="38" fill="var(--navy)"/>
      <rect x="0" y="98" width="216" height="42" fill="var(--red)"/>
    </g>
    <text class="brewery-line" x="108" y="30" text-anchor="middle" font-size="7" letter-spacing=".6" fill="var(--white)">GENTLE HARBOR BREWING</text>
    <text class="brand-name" x="108" y="62" text-anchor="middle" font-size="19">GENTLE</text>
    <text class="brand-name" x="108" y="91" text-anchor="middle" font-size="25">HARBOR</text>
    <text class="style-name" x="108" y="115" text-anchor="middle" font-size="8" letter-spacing="2.5">PALE ALE</text>
    <polygon fill="var(--navy)" points="24,73 25.8,77.6 30.6,77.6 26.7,80.5 28.1,85 24,82.2 19.9,85 21.3,80.5 17.4,77.6 22.2,77.6"/>
    <polygon fill="var(--navy)" points="192,73 193.8,77.6 198.6,77.6 194.7,80.5 196.1,85 192,82.2 187.9,85 189.3,80.5 185.4,77.6 190.2,77.6"/>
  </svg>

  <!-- Body label -->
  <svg class="body-label" viewBox="0 0 364 456" aria-label="Gentle Harbor body label, Pale Ale">
    <defs>
      <linearGradient id="shieldGold" x1="0" y1="0" x2="1" y2="1">
        <stop offset="0" stop-color="var(--gold-light)"/>
        <stop offset=".5" stop-color="var(--gold)"/>
        <stop offset="1" stop-color="var(--gold-light)"/>
      </linearGradient>
      <linearGradient id="riderTone" x1="0" y1="0" x2="0" y2="1">
        <stop offset="0" stop-color="#3a3a3a"/>
        <stop offset="1" stop-color="var(--ink)"/>
      </linearGradient>
      <clipPath id="shieldInner">
        <path d="M33,72 L329,72 L335,300 Q335,350 182,428 Q29,350 29,300 Z"/>
      </clipPath>
    </defs>

    <path class="shield-frame" d="M14,60 Q14,48 28,48 L336,48 Q350,48 350,60 L356,302 Q356,362 182,454 Q8,362 8,302 Z" fill="url(#shieldGold)"/>
    <path class="shield-face" d="M25,66 Q25,58 35,58 L329,58 Q339,58 339,66 L345,300 Q345,356 182,440 Q19,356 19,300 Z" fill="var(--white)"/>

    <g clip-path="url(#shieldInner)">
      <rect class="sky-panel" x="0" y="0" width="364" height="140" fill="var(--navy)"/>
      <g class="halo-rings" fill="none" stroke="var(--white)" stroke-width="11">
        <circle cx="182" cy="160" r="44"/>
        <circle cx="182" cy="160" r="68"/>
        <circle cx="182" cy="160" r="92"/>
      </g>
      <g class="chevrons" fill="none" stroke="var(--chevron)" stroke-width="22" stroke-linejoin="miter">
        <polyline points="20,220 182,150 344,220"/>
        <polyline points="20,262 182,192 344,262"/>
      </g>
      <rect class="base-panel" x="0" y="305" width="364" height="160" fill="var(--red)"/>
    </g>

    <rect class="mascot-art" x="118" y="68" width="128" height="124" rx="18" fill="url(#riderTone)" role="img" aria-label="Illustration: mascot riding a motorcycle toward the viewer"/>

    <text class="brand-name" x="182" y="238" text-anchor="middle" font-size="42">GENTLE</text>
    <text class="brand-name" x="182" y="296" text-anchor="middle" font-size="54">HARBOR</text>

    <text class="style-name" x="182" y="345" text-anchor="middle" font-size="14" letter-spacing="5">PALE ALE</text>
    <polygon fill="var(--white)" points="182,366 185.2,374.6 194.4,374.6 187,380.2 189.7,389 182,383.6 174.3,389 177,380.2 169.6,374.6 178.8,374.6"/>

    <path class="ribbon" d="M54,46 Q182,6 310,46" fill="none" stroke="url(#shieldGold)" stroke-width="28"/>
    <path id="ribbonLine" d="M54,51 Q182,11 310,51" fill="none"/>
    <text class="brewery-line" font-size="13" letter-spacing="1.2" fill="var(--navy)">
      <textPath href="#ribbonLine" startOffset="50%" text-anchor="middle">GENTLE HARBOR BREWING</textPath>
    </text>
  </svg>

</main>
</body>
</html>
```